Business Card for new Overseas Property Buying Business

Hi

We need a new business card for our new business.

We are Faraway Nest Seekers. So we search locations on behalf of our clients to find them the ideal home.

These are mainly holiday homes in nice locations - but sometimes people are looking to relocate.

I am looking for a nice simple design - that has some class and professionalism about it. Taking inspiration from our logo.

Text wise I was thinking of maybe having something like. (THE FONT FOR THIS SHOULD BE LIKE THE WRITING IN THE ATTACHMENT WITH THE MAP ON IT)

1)
What does your dream house have (tick all that apply):
swimming pool x
private vineyard x
herb garden x
full sized football pitch x

2)
How to buy a home abroad:

Method 1:
1) Scour internet for suitable estate agents
2) Arrange hectic holiday timetable with multiple agents in multiple languages
3) Fly to destination to find property was not as it seemed
4) Feel frustrated and helpless
OR
Method 2:
Contact your expert home hunter (details overleaf) - and leave the hard work to them

The end result should give people confidence that they are dealing with a professional organisation - and feel like they can place their trust in them. I would want it to drive them to either contact us directly or visit the website.

Please include name (Gordon Marsh), position (founder), contact numbers x 2, email address, website (www.quillan-tarvo.com)

I look forward to seeing your entries.

```html
<!DOCTYPE html>
<html lang="en">
<head>
<meta charset="utf-8">
<title>Quillan &amp; Tarvo – Business Card</title>
<link rel="stylesheet" href="https://fonts.googleapis.com/css2?family=Libre+Baskerville:wght@400;700&family=Titillium+Web:wght@400;600;700&display=swap">
<style>
  :root {
    --paper: #eeeeee;
    --paper-edge: #e6e6e6;
    --ink: #3b3b3b;
    --ink-soft: #2a2a2a;
    --brand-brown: #5a4e45;
    --brand-coral: #e2643f;
    --rule: #cfcfcf;
    --divider: #dcdcdc;
  }
  * { box-sizing: border-box; margin: 0; padding: 0; }
  html, body { width: 720px; height: 1200px; overflow: hidden; }
  body {
    background: var(--paper);
    font-family: "Titillium Web", sans-serif;
    color: var(--ink);
  }
  .card {
    position: relative;
    width: 720px;
    height: 1200px;
    background: radial-gradient(ellipse at 50% 40%, #f3f3f3 0%, var(--paper) 60%, var(--paper-edge) 100%);
  }
  .brand-mark {
    position: absolute;
    top: 114px;
    left: 255px;
  }
  .brand-name {
    position: absolute;
    top: 392px;
    left: 0;
    width: 720px;
    text-align: center;
    font-family: "Libre Baskerville", serif;
    font-size: 54px;
    font-weight: 400;
    line-height: 66px;
    color: var(--brand-brown);
  }
  .brand-rule {
    position: absolute;
    top: 460px;
    left: 144px;
    width: 441px;
    height: 2px;
    background: var(--brand-brown);
  }
  .brand-tagline {
    position: absolute;
    top: 466px;
    left: 0;
    width: 720px;
    text-align: center;
    font-family: "Libre Baskerville", serif;
    font-size: 23px;
    font-weight: 700;
    line-height: 30px;
    letter-spacing: 0.5px;
    color: var(--brand-brown);
  }
  .person-name {
    position: absolute;
    top: 664px;
    left: 0;
    width: 720px;
    text-align: center;
    font-size: 42px;
    font-weight: 600;
    line-height: 48px;
    color: var(--ink);
  }
  .contact-table {
    position: absolute;
    top: 722px;
    left: 167px;
    width: 398px;
    border-collapse: collapse;
  }
  .contact-table tr { border-bottom: 1px dashed var(--rule); }
  .contact-table tr:first-child { border-top: 1px dashed var(--rule); }
  .contact-table th,
  .contact-table td {
    vertical-align: middle;
    font-size: 22px;
    line-height: 1;
    color: var(--ink-soft);
  }
  .contact-table .row-mail th, .contact-table .row-mail td { height: 51px; }
  .contact-table .row-phone th, .contact-table .row-phone td { height: 56px; }
  .contact-table .row-mobile th, .contact-table .row-mobile td { height: 50px; }
  .contact-table .row-role th, .contact-table .row-role td { height: 43px; }
  .contact-table .row-web th, .contact-table .row-web td { height: 46px; }
  .contact-table th {
    width: 104px;
    text-align: left;
    font-weight: 700;
    padding-left: 4px;
    border-right: 1px solid var(--divider);
  }
  .contact-table td {
    padding-left: 11px;
    font-weight: 400;
  }
</style>
</head>
<body>
  <main class="card">
    <svg class="brand-mark" width="220" height="220" viewBox="0 0 220 220" aria-hidden="true">
      <circle cx="110" cy="110" r="108" fill="var(--brand-coral)"/>
    </svg>
    <p class="brand-name">Quillan &amp; Tarvo</p>
    <div class="brand-rule"></div>
    <p class="brand-tagline">FARAWAY NEST SEEKERS</p>

    <h1 class="person-name">GORDON MARSH</h1>

    <table class="contact-table">
      <tr class="row-mail"><th>Mail:</th><td>info@quillan-tarvo.com</td></tr>
      <tr class="row-phone"><th>Phone:</th><td>020 7946 0321</td></tr>
      <tr class="row-mobile"><th>Mobile:</th><td>07700 900 412</td></tr>
      <tr class="row-role"><th>Charge:</th><td>Founder</td></tr>
      <tr class="row-web"><th>www:</th><td>www.quillan-tarvo.com</td></tr>
    </table>
  </main>
</body>
</html>
```